App Design for quiz app (casual gaming app)

We need an design & logo for our quiz app. Its a simple quiz app, where you pick up a category, answer three questions out of this category. After this an opponent is assigned to your game, and has to answer the same three questions. After this first round is finished, it's the opponents turn to choose a new category and answer three questions out of this category. Now it's your turn to answer the same three questions. With this done, the 2nd round is finished. One game has seven rounds.
Please find attached the balsamiq project. For all of you, do not have balsamiq, please find also the mockups as pdf.
Final delivery should be psd files
Target Market(s)
Casual Games

```html
<!DOCTYPE html>
<html lang="en">
<head>
<meta charset="utf-8">
<title>QuizNest – Question</title>
<link rel="stylesheet" href="https://fonts.googleapis.com/css2?family=Figtree:wght@400;500;600&display=swap">
<style>
  :root {
    --green: #5db872;
    --green-light: #7ec68f;
    --white: #ffffff;
    --ink: #454545;
    --option-bg: #e5efed;
    --option-edge: #cddbd8;
    --option-text: #6d9a93;
    --active-bg: #70a098;
    --active-edge: #56857d;
  }
  * { margin: 0; padding: 0; box-sizing: border-box; }
  html, body {
    width: 733px;
    height: 1200px;
    overflow: hidden;
    background: var(--white);
    font-family: "Figtree", "Helvetica Neue", Arial, sans-serif;
  }
  .screen {
    position: relative;
    width: 733px;
    height: 1200px;
    background: var(--white);
  }
  .app-header {
    position: relative;
    height: 168px;
    color: var(--white);
    overflow: hidden;
  }
  .app-header .header-bg {
    position: absolute;
    inset: 0;
  }
  .status-bar {
    position: relative;
    height: 50px;
    display: flex;
    align-items: center;
    justify-content: space-between;
    padding: 0 24px 0 22px;
    font-size: 20px;
    font-weight: 500;
  }
  .status-left, .status-right {
    display: flex;
    align-items: center;
    gap: 8px;
    width: 200px;
  }
  .status-right { justify-content: flex-end; }
  .status-time {
    position: absolute;
    left: 0; right: 0;
    text-align: center;
  }
  .nav-bar {
    position: relative;
    height: 118px;
    display: flex;
    align-items: center;
    justify-content: center;
    padding-bottom: 16px;
  }
  .menu-button {
    position: absolute;
    left: 60px;
    top: 44px;
    width: 39px;
    height: 28px;
  }
  .app-title {
    font-size: 35px;
    font-weight: 400;
    letter-spacing: 0.3px;
  }
  .question {
    margin-top: 91px;
    text-align: center;
    font-size: 42px;
    font-weight: 500;
    line-height: 56px;
    color: var(--ink);
  }
  .answers {
    list-style: none;
    margin: 94px auto 0;
    width: 519px;
  }
  .answer {
    height: 74px;
    margin-bottom: 52px;
    border-radius: 13px;
    background: var(--option-bg);
    box-shadow: 0 3px 0 var(--option-edge);
    display: flex;
    align-items: center;
    justify-content: center;
    font-size: 31px;
    font-weight: 500;
    color: var(--option-text);
  }
  .answer.is-selected {
    background: var(--active-bg);
    box-shadow: 0 3px 0 var(--active-edge);
    color: var(--white);
  }
</style>
</head>
<body>
<main class="screen">
  <header class="app-header">
    <svg class="header-bg" width="733" height="168" viewBox="0 0 733 168" aria-hidden="true">
      <rect width="733" height="168" fill="var(--green-light)"/>
      <polygon points="0,0 375,0 438,168 0,168" fill="var(--green)"/>
    </svg>
    <div class="status-bar">
      <div class="status-left">
        <svg width="66" height="12" viewBox="0 0 66 12" aria-hidden="true">
          <circle cx="6" cy="6" r="5" fill="#fff"/>
          <circle cx="19" cy="6" r="5" fill="#fff"/>
          <circle cx="32" cy="6" r="5" fill="#fff"/>
          <circle cx="45" cy="6" r="4.3" fill="none" stroke="#fff" stroke-width="1.3"/>
          <circle cx="58" cy="6" r="4.3" fill="none" stroke="#fff" stroke-width="1.3"/>
        </svg>
        <span class="carrier">VOLT</span>
        <svg width="22" height="16" viewBox="0 0 22 16" aria-hidden="true">
          <path d="M1 5.5a14 14 0 0 1 20 0" fill="none" stroke="#fff" stroke-width="2.2" stroke-linecap="round"/>
          <path d="M4.5 9a9 9 0 0 1 13 0" fill="none" stroke="#fff" stroke-width="2.2" stroke-linecap="round"/>
          <path d="M11 15l-3-3a4.3 4.3 0 0 1 6 0z" fill="#fff"/>
        </svg>
      </div>
      <span class="status-time">4:21 PM</span>
      <div class="status-right">
        <svg width="12" height="20" viewBox="0 0 12 20" aria-hidden="true">
          <path d="M1 5.5l9 8-4.5 4V2.5l4.5 4-9 8" fill="none" stroke="#fff" stroke-width="1.5" stroke-linejoin="round" opacity="0.85"/>
        </svg>
        <span class="battery-level">100%</span>
        <svg width="46" height="18" viewBox="0 0 46 18" aria-hidden="true">
          <rect x="1" y="1" width="40" height="16" rx="3" fill="none" stroke="#fff" stroke-width="1.5"/>
          <rect x="3" y="3" width="36" height="12" rx="1.5" fill="#fff"/>
          <rect x="42.5" y="6" width="2.5" height="6" rx="1" fill="#fff"/>
        </svg>
      </div>
    </div>
    <nav class="nav-bar">
      <svg class="menu-button" viewBox="0 0 39 28" aria-label="Menu" role="img">
        <rect y="0" width="39" height="3" fill="#fff"/>
        <rect y="12.5" width="39" height="3" fill="#fff"/>
        <rect y="25" width="39" height="3" fill="#fff"/>
      </svg>
      <h1 class="app-title">QuizNest</h1>
    </nav>
  </header>

  <section class="quiz-card">
    <h2 class="question">Who was<br>Harold Whitcombe?</h2>
    <ul class="answers">
      <li class="answer">Football Player</li>
      <li class="answer is-selected">Actor</li>
      <li class="answer">World War 2 General</li>
      <li class="answer">Musician</li>
    </ul>
  </section>
</main>
</body>
</html>
```